International business needs a web page design

We need a web page design for a new service that our new "sub-company" of our existing company will offer. We are based in Denmark, and our new "sub-company" is called 'Velkari'. The service we offer is automated server configuration and In-Depth monitoring, and optional operations support. Our monitoring has a lot of graphs (like those seen here: https://velkari.example/ with either black or white background ) and the website needs to communicate a sense of Security/safety and that our customers can relax, because we have the full overview of their service and servers. The website should not be with black background.

We deliver low price, high quality and professional operations - which we can do, because we automate it and have people with 15+ years of experience doing so.

We have attached :

Target Market(s)

Chief Technological officers (CTO's) and Developers (small business, run by developers) - who needs professional IT operations.

Industry/Entity Type

Business

Coding

Coded - Design and coding required

Number of Pages Required

3 page

Requirements
Must have
• Frontpage :
• A lot of visualization(some with people too) rather than a lot of text
• A short, describing text on front page telling what people get
• 3 steps showing people how it works. (Could be presented in a video placed on top of a big front image or perhaps with all 3 steps/pictures shown at the same time or perhaps in a completely different way).
Nice to have
• A big front image(perhaps a person with a cellphone showing graphs and a "all okay" message) with a text and the 3-steps pictures/or video on top of it
• 3 boxes under the front image/top of the site showing what benefits people get from the service
Should not have
• Not a black/dark site

```html
<!DOCTYPE html>
<html lang="en">
<head>
<meta charset="utf-8">
<title>Velkari – Instant server setup &amp; in-depth monitoring</title>
<link rel="stylesheet" href="https://fonts.googleapis.com/css2?family=Open+Sans:wght@400;600;700&display=swap">
<style>
:root{
  --blue:#0b8dcd;
  --blue-dark:#0779b3;
  --green:#5cb533;
  --ink:#2f3538;
  --muted:#7b8388;
  --band:#eceff1;
  --footer:#343b40;
  --white:#ffffff;
}
*{margin:0;padding:0;box-sizing:border-box}
html,body{width:686px;height:1200px;overflow:hidden;background:var(--white)}
body{font-family:"Open Sans",Arial,sans-serif;color:var(--ink);position:relative}
.abs{position:absolute}

/* header */
.site-header{left:0;top:0;width:686px;height:43px;background:var(--white)}
.brand{left:108px;top:6px;display:flex;align-items:center;gap:6px}
.brand-dot{width:32px;height:32px;border-radius:50%;background:var(--blue)}
.brand-name{font-size:20px;font-weight:700;color:var(--ink);line-height:1}
.brand-tag{font-size:6px;font-weight:600;color:var(--ink);margin-top:2px}
.main-nav{left:0;top:0;width:500px;height:43px;font-size:7.5px;color:#7d8589}
.main-nav a{position:absolute;top:15px;color:inherit;text-decoration:none;white-space:nowrap}
.main-nav a.is-active{color:var(--blue)}
.login-btn{left:504px;top:11px;width:36px;height:18px;background:var(--green);color:var(--white);font-size:6.5px;font-weight:600;text-align:center;line-height:18px}
.social-dots{left:551px;top:16px;display:flex;gap:5px}
.social-dots span{width:7px;height:7px;border-radius:50%;background:#6f777c}

/* hero */
.hero{left:0;top:43px;width:686px;height:301px;background:linear-gradient(160deg,#0c98d6 0%,#0a86c4 60%,#0a7fbd 100%);overflow:hidden}
.hero-backdrop{left:0;top:0;width:300px;height:301px;background:linear-gradient(180deg,rgba(0,63,107,0) 35%,rgba(0,63,107,.14) 100%)}
.hero-photo{left:300px;top:0;width:386px;height:301px;background:linear-gradient(120deg,rgba(170,210,235,.0) 0%,rgba(150,200,232,.55) 35%,rgba(205,228,244,.8) 70%,rgba(180,215,238,.7) 100%)}
.hero-title{left:126px;top:57px;font-size:15.5px;font-weight:700;color:var(--white);line-height:19px;letter-spacing:.2px}
.hero-points{left:126px;top:104px;list-style:none;color:var(--white);font-size:8.6px}
.hero-points li{display:flex;align-items:center;gap:7px;height:16px}
.hero-points svg{flex:none}
.hero-cta{left:125px;top:159px;width:165px;height:23px;background:var(--green);color:var(--white);font-size:7px;font-weight:600;text-align:center;line-height:23px}

/* benefits */
.benefits{left:0;top:344px;width:686px;height:169px;background:var(--band)}
.benefit{top:0;width:150px;text-align:center}
.benefit-icon{margin:-8px auto 0;width:82px;height:82px;border-radius:50%;background:var(--band);display:flex;align-items:center;justify-content:center}
.benefit-icon div{width:68px;height:68px;border-radius:50%;background:var(--blue);display:flex;align-items:center;justify-content:center}
.benefit h3{font-size:10px;font-weight:600;color:var(--ink);height:28px;display:flex;align-items:flex-end;justify-content:center;line-height:13px;margin-top:9px}
.benefit p{font-size:6px;color:var(--muted);line-height:10.3px;margin:7px -2px 0;letter-spacing:-.05px}

/* demo */
.demo{left:0;top:513px;width:686px;height:282px;background:linear-gradient(#ffffff 0%,#eef6fc 45%,#d9ecf8 100%);overflow:hidden}
.demo-kicker{left:0;top:14px;width:686px;text-align:center;font-size:13px;color:var(--ink)}
.demo-title{left:0;top:33px;width:686px;text-align:center;font-size:17px;font-weight:700;color:var(--ink)}
.demo-title em{font-style:normal;color:var(--blue)}
.demo-text{left:126px;top:58px;width:434px;text-align:center;font-size:6.3px;color:var(--muted);line-height:10.3px}
.demo-cta{left:306px;top:87px;width:74px;height:21px;background:var(--green);color:var(--white);font-size:7px;font-weight:600;text-align:center;line-height:21px}
.skyline{left:0;top:120px;width:686px;height:162px;background:linear-gradient(rgba(255,255,255,0),#bfe0f4 40%,#7fbfe6 100%)}
.screen{background:#1f2326;border:1px solid #9aa3a8}
.screen-bar{height:9px;background:#d8dcde}
.screen-body{position:absolute;left:0;right:0;top:9px;bottom:0;background:linear-gradient(135deg,#2a2f33,#1b1f22)}
.screen-light .screen-body{background:linear-gradient(135deg,#f4f6f7,#e3e7ea)}

/* testimonials */
.love{left:0;top:795px;width:686px;height:236px;background:var(--band)}
.love h2{position:absolute;left:0;top:23px;width:686px;text-align:center;font-size:16.5px;font-weight:700;color:var(--ink)}
.quote{left:153px;top:65px;width:175px;height:118px;background:var(--blue);color:var(--white);font-size:8.3px;line-height:13.2px;padding:19px 15px 0 20px;text-align:justify}
.avatar{left:172px;top:163px;width:54px;height:54px;border-radius:50%;background:linear-gradient(#e9d3c4,#b98b70);border:3px solid var(--white)}
.person{font-size:7.3px}
.person strong{display:block;font-weight:700;color:var(--ink)}
.person span{color:var(--blue);font-size:6.4px}
.video{left:358px;top:65px;width:175px;height:118px;background:linear-gradient(135deg,#d9d3c9,#b9aa95 60%,#9c8f7d)}
.play{left:72px;top:43px;width:33px;height:33px;border-radius:50%;background:var(--white);display:flex;align-items:center;justify-content:center}
.arrow{top:115px}

/* footer */
.site-footer{left:0;top:1031px;width:686px;height:125px;background:var(--footer);color:#b7bdc1}
.footer-about h4{font-size:9.5px;font-weight:600;color:var(--blue);margin-bottom:8px}
.footer-about p{font-size:6.3px;line-height:10.3px;width:155px}
.footer-brand{left:286px;top:26px;display:flex;align-items:center;gap:6px}
.footer-brand .brand-dot{background:#555d62}
.footer-brand .brand-name{color:#5a6267}
.footer-brand .brand-tag{color:#59636a;font-size:5px}
.footer-nav{left:291px;top:64px;font-size:6.8px;display:flex;gap:13px;color:#c4c9cc}
.footer-cta{left:281px;top:81px;width:144px;height:19px;background:var(--blue);color:var(--white);font-size:6.4px;font-weight:600;text-align:center;line-height:19px}
.contact{left:448px;top:40px;font-size:6.6px;color:#c4c9cc}
.contact li{list-style:none;display:flex;align-items:center;gap:7px;height:16px}
.contact .rings{display:flex;gap:5px;margin-top:3px}
.contact .rings span{width:12px;height:12px;border-radius:50%;border:1px solid var(--blue)}
.contact li.copyright{display:block;line-height:16px;margin-top:6px}
.copyright a{color:var(--blue);text-decoration:none}
</style>
</head>
<body>

<header class="site-header abs">
  <div class="brand abs">
    <div class="brand-dot"></div>
    <div>
      <div class="brand-name">Velkari</div>
      <div class="brand-tag">Instant server setup &amp; In-depth monitoring</div>
    </div>
  </div>
  <nav class="main-nav abs">
    <a class="is-active" href="#" style="left:328px">HOME</a>
    <a href="#" style="left:364px">SERVICES</a>
    <a href="#" style="left:411px">ABOUT US</a>
    <a href="#" style="left:462px">SUPPORT</a>
  </nav>
  <div class="login-btn abs">LOGIN</div>
  <div class="social-dots abs"><span></span><span></span><span></span></div>
</header>

<section class="hero abs">
  <div class="hero-backdrop abs" role="img" aria-label="Faint network of connected data points"></div>
  <div class="hero-photo abs" role="img" aria-label="Smiling man on the phone holding a laptop showing monitoring status with all checks green"></div>
  <h1 class="hero-title abs">INSTANT SERVER SETUP AND<br>IN-DEPTH MONITORING</h1>
  <ul class="hero-points abs">
    <li><svg width="10" height="10" viewBox="0 0 10 10"><circle cx="5" cy="5" r="4.3" fill="none" stroke="#fff" stroke-width=".9"/><path d="M4 3l2 2-2 2" fill="none" stroke="#fff" stroke-width=".9"/></svg>Lorem ipsum dolor sit amet, consectetur adipiscing elit.</li>
    <li><svg width="10" height="10" viewBox="0 0 10 10"><circle cx="5" cy="5" r="4.3" fill="none" stroke="#fff" stroke-width=".9"/><path d="M4 3l2 2-2 2" fill="none" stroke="#fff" stroke-width=".9"/></svg>Proin efficitur ipsum non condimentum tincidunt.</li>
    <li><svg width="10" height="10" viewBox="0 0 10 10"><circle cx="5" cy="5" r="4.3" fill="none" stroke="#fff" stroke-width=".9"/><path d="M4 3l2 2-2 2" fill="none" stroke="#fff" stroke-width=".9"/></svg>Ut sollicitudin lorem commodo est.</li>
  </ul>
  <div class="hero-cta abs">CLICK TO GET INSTANT SERVER SETUP NOW</div>
</section>

<section class="benefits abs">
  <article class="benefit abs" style="left:104px">
    <div class="benefit-icon"><div>
      <svg width="32" height="32" viewBox="0 0 32 32" aria-hidden="true"><path d="M26 6c-7 0-12 5-15 11l4 4c6-3 11-8 11-15z" fill="#fff"/><path d="M11 17l-5 1 4-5h4zM15 21l-1 5 5-4v-4z" fill="#fff"/><path d="M9 21l-4 6 6-4z" fill="#fff"/><circle cx="20" cy="12" r="2" fill="#0b8dcd"/></svg>
    </div></div>
    <h3>It is fast and easy</h3>
    <p>Ras facilisis pulvinar tincidunt. Maecenas bibendum varius suscipit. Quisque sit amet quam a est ornare interdum. Duis lacus mauris, consequat at massa non, posuere consequat dolor.</p>
  </article>
  <article class="benefit abs" style="left:268px">
    <div class="benefit-icon"><div>
      <svg width="34" height="34" viewBox="0 0 34 34" aria-hidden="true"><path d="M17 2l3.5 3 4.5-.5 1.5 4.3 4 2.2-1 4.5 2 4-3.5 3-.5 4.5-4.5.7L20 31l-3-1.5L14 31l-3-3.3-4.5-.7L6 22.5l-3.5-3 2-4-1-4.5 4-2.2L9 4.5l4.5.5z" fill="#fff"/><circle cx="17" cy="17" r="9" fill="none" stroke="#0b8dcd" stroke-width="1.6"/><path d="M12.5 17l3 3 6-6" fill="none" stroke="#0b8dcd" stroke-width="2.2"/></svg>
    </div></div>
    <h3>Relax &amp; Rest Assured</h3>
    <p>Ras facilisis pulvinar tincidunt. Maecenas bibendum varius suscipit. Quisque sit amet quam a est ornare interdum. Duis lacus mauris, consequat at massa non, posuere consequat dolor.</p>
  </article>
  <article class="benefit abs" style="left:432px">
    <div class="benefit-icon"><div>
      <svg width="34" height="34" viewBox="0 0 34 34" aria-hidden="true"><path d="M17 18c-5-4-7-6-7-9a3.5 3.5 0 0 1 7-1 3.5 3.5 0 0 1 7 1c0 3-2 5-7 9z" fill="#fff"/><path d="M4 21h5l6 2h5a1.5 1.5 0 0 1 0 3h-5 6l6-4a1.6 1.6 0 0 1 2 2.4L22 30H9l-5-2z" fill="#fff"/></svg>
    </div></div>
    <h3>You'll love your<br>detailed performance graph</h3>
    <p>Ras facilisis pulvinar tincidunt. Maecenas bibendum varius suscipit. Quisque sit amet quam a est ornare interdum. Duis lacus mauris, consequat at massa non, posuere consequat dolor.</p>
  </article>
</section>

<section class="demo abs">
  <p class="demo-kicker abs">Sign Up to</p>
  <h2 class="demo-title abs">GET THE <em>FREE</em> DEMO</h2>
  <p class="demo-text abs">Ras facilisis pulvinar tincidunt. Maecenas bibendum varius suscipit. Quisque sit amet quam a est ornare interdum. Duis lacus mauris, consequat at massa non, posuere consequat dolor.</p>
  <div class="demo-cta abs">SIGN UP NOW!</div>
  <div class="skyline abs" role="img" aria-label="Soft clouds over a blue city skyline"></div>
  <div class="screen abs" style="left:108px;top:153px;width:110px;height:129px"><div class="screen-bar"></div><div class="screen-body" role="img" aria-label="Monitoring dashboard with dark graph panels"></div></div>
  <div class="screen screen-light abs" style="left:468px;top:153px;width:110px;height:129px"><div class="screen-bar"></div><div class="screen-body" role="img" aria-label="Service status table on a light dashboard"></div></div>
  <div class="screen abs" style="left:213px;top:130px;width:260px;height:152px"><div class="screen-bar"></div><div class="screen-body" role="img" aria-label="Grid of server performance graphs on a dark dashboard"></div></div>
</section>

<section class="love abs">
  <h2>WHY PEOPLE LOVE US</h2>
  <svg class="arrow abs" style="left:106px" width="24" height="42" viewBox="0 0 24 42" aria-hidden="true"><path d="M22 1L2 21l20 20" fill="none" stroke="#a9b0b4" stroke-width="1.2"/></svg>
  <svg class="arrow abs" style="left:556px" width="24" height="42" viewBox="0 0 24 42" aria-hidden="true"><path d="M2 1l20 20L2 41" fill="none" stroke="#a9b0b4" stroke-width="1.2"/></svg>
  <blockquote class="quote abs">“Cras facilisis pulvinar tincidunt. Maecenas bibendum varius suscipit. Quisque sit amet quam a est ornare interdum. Duis lacus mauris, cons equat at massa non,</blockquote>
  <svg class="abs" style="left:228px;top:183px" width="12" height="10" viewBox="0 0 12 10" aria-hidden="true"><path d="M0 0h12L12 10z" fill="#0b8dcd"/></svg>
  <div class="avatar abs" role="img" aria-label="Portrait of John Smith"></div>
  <div class="person abs" style="left:242px;top:191px"><strong>JOHN SMITH</strong><span>New York, A Lorem Ipsum Co.</span></div>
  <div class="video abs" role="img" aria-label="Video testimonial from Miss Rita">
    <div class="play abs"><svg width="14" height="16" viewBox="0 0 14 16" aria-hidden="true"><path d="M2 1l11 7-11 7z" fill="#0b8dcd"/></svg></div>
  </div>
  <div class="person abs" style="left:363px;top:191px"><strong>MISS RITA</strong><span>London Heathrow, A Lorem Ipsum Co.</span></div>
</section>

<footer class="site-footer abs">
  <div class="footer-about abs" style="left:108px;top:29px">
    <h4>ABOUT VELKARI</h4>
    <p>Cras facilisis pulvinar tincidunt. Maecenas bibendum varius suscipit. Quisque sit amet quam a est ornare interdum. Duis lacus mauris, consequat at massa non, posuere consequat dolor. Proin sit amet dolor eu mauris mattis tempus eget sed risus.</p>
  </div>
  <div class="footer-brand abs">
    <div class="brand-dot"></div>
    <div>
      <div class="brand-name">Velkari</div>
      <div class="brand-tag">Instant server setup &amp; In-depth monitoring</div>
    </div>
  </div>
  <nav class="footer-nav abs"><span>Home</span><span>Services</span><span>About Us</span><span>Support</span></nav>
  <div class="footer-cta abs">CLICK TO GET INSTANT SERVER SETUP NOW</div>
  <ul class="contact abs">
    <li><svg width="8" height="10" viewBox="0 0 8 10" aria-hidden="true"><path d="M4 0a4 4 0 0 1 4 4c0 3-4 6-4 6S0 7 0 4a4 4 0 0 1 4-4z" fill="#0b8dcd"/><circle cx="4" cy="4" r="1.4" fill="#343b40"/></svg>150, Lorem Ipsum, Dolor Sit, United State</li>
    <li><svg width="8" height="6" viewBox="0 0 8 6" aria-hidden="true"><rect width="8" height="6" fill="#0b8dcd"/><path d="M0 0l4 3 4-3" fill="none" stroke="#343b40" stroke-width=".8"/></svg>support@velkari.example</li>
    <li class="rings"><span></span><span></span><span></span></li>
    <li class="copyright">Copyright 2014 by <a href="https://velkari.example/">velkari.example</a></li>
  </ul>
</footer>

</body>
</html>
```